web design needed for jewellery inspired temporary tattoo company

Hi There

I need a web design for a new company I'm launching called coral glow luxe
Im a retailer of flash tattoos - temporary gold and silver metallic tattoos

These are the next new craze with many celebrities already displaying them whilst being lapped on their holidays

i need a very classy upmarket wow web design with an e commerce shop attached

I also offer marlow q bronze mist so will need a page to link to where people can get a tan and tattoo - so maybe as a box on the main page

As A guide I'm looking for someone to put their unique spin on an american website which is currently selling the same type of product
www.glintmarkz.com

the final design should oozzzz 'rich list ' coral luxe - think st tropez Monaco and needs to be linked to all my social media

please seepintrest flash tattoos for what we sell
I've attached my logo

I can't wait to hear from you all
many Thanks

Fiona Dembrey
www.coralglowluxe.co.uk

Target Market(s)

20 to 30's young party rich list glamous girls - festival boho cool beach LA

Industry/Entity Type

It Company

Number of Pages Required

3 page

Font styles to use
Script

Requirements
Must have
• a beach feel
• pictures of people wearing the tattoos
• an ecommerce site
• be easy to navigate
• my logo
• the wow factor
Nice to have
• a really classy expensive feel to the website
Should not have
• a cheap plain look

```html
<!DOCTYPE html>
<html lang="en">
<head>
<meta charset="utf-8">
<title>Coral Glow Luxe — Flash Tattoos</title>
<link rel="stylesheet" href="https://fonts.googleapis.com/css2?family=Open+Sans:ital,wght@0,300;0,400;0,600;0,700;1,300&display=swap">
<style>
  :root {
    --ink: #111111;
    --text: #333333;
    --muted: #777777;
    --rule: #d6d6d6;
    --white: #ffffff;
    --sea-light: #e4ecee;
    --sea: #c9dde0;
    --sand: #e8d9c4;
    --skin: #b98a6a;
    --cream: #f3efdf;
    --stone: #e2e2e0;
  }
  * { margin: 0; padding: 0; box-sizing: border-box; }
  html, body { width: 1200px; height: 947px; overflow: hidden; background: var(--white); }
  body { font-family: "Open Sans", Arial, sans-serif; color: var(--text); position: relative; }

  .brand-mark {
    position: absolute; left: 30px; top: 0; width: 142px; height: 136px;
    background: var(--ink); display: flex; align-items: center; justify-content: center;
    text-align: center; color: var(--white); font-size: 15px; font-weight: 400; line-height: 1.3;
  }

  .utility-nav {
    position: absolute; right: 30px; top: 16px; font-size: 13px; color: var(--text);
    display: flex; gap: 11px; align-items: center;
  }
  .utility-nav .sep { color: var(--muted); }
  .utility-nav .caret { width: 8px; height: 5px; margin-left: 6px; }
  .utility-nav .currency { margin-left: 10px; display: flex; align-items: center; gap: 4px; }
  .utility-nav .flag { width: 14px; height: 9px; background: #5a6fa8; display: inline-block; }

  .contact-line {
    position: absolute; right: 30px; top: 69px; font-size: 20px; font-weight: 300; color: var(--text);
    display: flex; gap: 22px; align-items: center;
  }
  .contact-line span { display: flex; align-items: center; gap: 8px; }

  .header-rule { position: absolute; left: 30px; right: 30px; top: 135px; border-top: 1px solid var(--rule); }

  .main-nav {
    position: absolute; left: 29px; top: 156px; display: flex; gap: 54px;
    font-size: 16px; font-weight: 400; text-transform: uppercase; color: var(--ink);
  }
  .search {
    position: absolute; left: 943px; top: 156px; width: 227px; display: flex; justify-content: space-between; align-items: center;
    font-size: 16px; font-style: italic; font-weight: 300; color: #999;
  }

  .hero {
    position: absolute; left: 30px; top: 198px; width: 1140px; height: 456px;
    background: linear-gradient(90deg, var(--sea-light) 0%, var(--sea-light) 42%, var(--sea) 62%, var(--sand) 78%, var(--skin) 92%, var(--sea) 100%);
  }
  .hero-copy { position: absolute; left: 58px; top: 170px; color: var(--ink); }
  .hero-copy h1 { font-size: 27px; font-weight: 600; letter-spacing: 1.2px; line-height: 36px; }
  .hero-copy p { font-size: 16px; font-weight: 600; letter-spacing: .5px; margin-top: 2px; }
  .btn {
    display: inline-flex; align-items: center; gap: 12px; margin-top: 16px;
    background: var(--ink); color: var(--white); font-size: 16px; font-weight: 600; letter-spacing: 1px;
    height: 33px; padding: 0 14px 0 13px; text-transform: uppercase;
  }
  .slider-dots { position: absolute; left: 60px; top: 416px; display: flex; gap: 6px; }
  .slider-dots i { width: 10px; height: 10px; border-radius: 50%; background: #9aa3a6; display: block; }
  .slider-dots i.active { background: var(--ink); }

  .shipping-band {
    position: absolute; left: 30px; top: 674px; width: 1140px; height: 44px; background: var(--ink);
    color: var(--white); font-size: 19px; font-weight: 300; letter-spacing: 3.4px; text-align: center; line-height: 44px;
  }

  .promo { position: absolute; top: 738px; width: 375px; height: 197px; }
  .promo-1 { left: 30px; background: linear-gradient(90deg, #8a6448 0%, #b4906e 30%, var(--cream) 55%, var(--cream) 100%); }
  .promo-2 { left: 413px; background: linear-gradient(90deg, #d9cfb6 0%, #a98466 30%, #b08f72 45%, var(--cream) 65%); }
  .promo-3 { left: 795px; background: linear-gradient(90deg, #4a3a30 0%, #8f6c52 25%, #c8b8a6 45%, var(--stone) 60%); }
  .promo-copy { position: absolute; right: 21px; text-align: right; color: var(--ink); }
  .promo-copy h2 { font-size: 19px; font-weight: 600; letter-spacing: 1px; line-height: 24px; }
  .promo-copy h2 .big { font-size: 26px; display: block; line-height: 30px; }
  .promo-copy p { font-size: 13px; font-weight: 600; color: #6b6b6b; line-height: 16px; margin-top: 4px; }
</style>
</head>
<body>
  <div class="brand-mark">Coral Glow<br>Luxe</div>

  <nav class="utility-nav">
    <span>Home</span><span class="sep">|</span>
    <span>Gift Certificates</span><span class="sep">|</span>
    <span>Sign In og Create An Account</span><span class="sep">|</span>
    <span>View Cart : 0<svg class="caret" viewBox="0 0 8 5"><path d="M0 0h8L4 5z" fill="#333"/></svg></span>
    <span class="currency">All prices are in : <i class="flag"></i> USD<svg class="caret" viewBox="0 0 8 5"><path d="M0 0h8L4 5z" fill="#333"/></svg></span>
  </nav>

  <div class="contact-line">
    <span><svg width="17" height="17" viewBox="0 0 24 24"><path fill="#333" d="M6.6 10.8a15.2 15.2 0 0 0 6.6 6.6l2.2-2.2c.3-.3.7-.4 1-.2 1.1.4 2.3.6 3.6.6.6 0 1 .4 1 1V20c0 .6-.4 1-1 1A17 17 0 0 1 3 4c0-.6.4-1 1-1h3.5c.6 0 1 .4 1 1 0 1.3.2 2.5.6 3.6.1.3 0 .7-.2 1z"/></svg>Call Us : 5550 1234 56</span>
    <span><svg width="26" height="18" viewBox="0 0 26 18"><rect x="1" y="1" width="24" height="16" fill="none" stroke="#333" stroke-width="2"/><path d="M1 1l12 9 12-9M1 17l9-8M25 17l-9-8" fill="none" stroke="#333" stroke-width="2"/></svg>Mail Us : info@coralglowluxe.co.uk</span>
  </div>

  <div class="header-rule"></div>

  <nav class="main-nav">
    <span>Shop</span><span>About</span><span>Contact</span><span>Store Locator</span>
  </nav>
  <div class="search">
    <span>Type here to search</span>
    <svg width="25" height="25" viewBox="0 0 25 25"><circle cx="10" cy="10" r="8" fill="none" stroke="#555" stroke-width="2"/><path d="M16 16l7 7" stroke="#555" stroke-width="2.5"/></svg>
  </div>

  <section class="hero">
    <div class="hero-photo" role="img" aria-label="Woman on the beach seen from behind, wearing gold flash tattoos on her arms and back" style="position:absolute;inset:0"></div>
    <div class="hero-copy">
      <h1>RETAILER OF FLASH TATTOOS</h1>
      <p>Temporary gold and silver metallic tattoos</p>
      <span class="btn">Book Now <svg width="6" height="8" viewBox="0 0 6 8"><path d="M0 0l6 4-6 4z" fill="#fff"/></svg></span>
    </div>
    <div class="slider-dots"><i></i><i class="active"></i><i></i></div>
  </section>

  <div class="shipping-band">FREE SHIPPING ON ALL DOMESTIC ORDERS OVER $ 88</div>

  <article class="promo promo-1" role="img" aria-label="Tanned woman's back with a gold arrow flash tattoo along the spine">
    <div class="promo-copy" style="top:16px">
      <h2>MARLOW Q<span class="big">BRONZE MIST</span></h2>
      <p>TEMPORARY GOLD &amp; SILVER<br>METALLIC TATTOOS</p>
    </div>
  </article>

  <article class="promo promo-2" role="img" aria-label="Woman on the shore from behind with a gold flash tattoo down her back">
    <div class="promo-copy" style="top:82px">
      <h2>RETAILER OF<br>FLASH TATTOOS</h2>
      <p>TEMPORARY GOLD &amp; SILVER<br>METALLIC TATTOOS</p>
    </div>
  </article>

  <article class="promo promo-3" role="img" aria-label="Woman's back with a silver and gold chain flash tattoo">
    <div class="promo-copy" style="top:18px">
      <h2>RETAILER OF<br>FLASH TATTOOS</h2>
      <p>TEMPORARY GOLD &amp; SILVER<br>METALLIC TATTOOS</p>
    </div>
  </article>
</body>
</html>
```